Typographic word art illustration of life lessons

I've written out all the meaningful life lessons my parents have taught me and would like to give it to them for Christmas in the form of a typographic word art design. This will be a print project. I'd like the size of the design to be no larger than 11x17, no smaller than 8.5x11.
The text must be readable in the complete sentences provided.
The text can be displayed in multiple directions, as long as each sentence is readable.
The text itself should be arranged in an artistic and creative way. I'm not looking for text that is aligned in normal-looking rows with a an image watermark behind it.
Sentences may be included on the same row if it works with the design.
Font, Case and Text may be alternated to best suite your design. No grunge fonts, or small-size handwriting fonts, or anything that is difficult to read.
Text could fit into a shape or silhouette (ie: heart, tree, or anything that symbolizes family, life, love, etc.), or form an abstract design, or it can be justified to fit the whole page.
I'm not looking for anything super colorful. Black and white would work, or any standard color palette. The intended result is something they can hang on their wall.
Text is attached in a pdf. Minor tweaks to text is ok if necessary for formatting design, but in general, text should remain unedited.
I've also added some examples of the type of word art I had in mind.
Please help me make this gift into something beautiful and special!
Updates
I trimmed the text down significantly because all the designs seemed to crowded, and had to use fonts that were too small. Here is the revised text:
Don’t give up until you’ve given your all.
Don’t let people that hurt you occupy your mind.
Good people do bad things. Get over it.
Block bitterness from ever taking root in your heart.
Take every opportunity to express gratitude.
True brotherhood is forged out of loyalty and love.
There is no excuse for deceit.
Words matter.
Forgiveness is not optional.
Never make insincere apologies.
Worrying is a waste of time.
Choose your destiny by choosing your friends.
Marriage is a unified front. Make your spouse a priority.
Truth and grace are inseparable.
Humor disarms, softens and endears.
Selflessness is a lifestyle.
Whenever possible, give generously and anonymously.
Never apologize and give an excuse in the same sentence.
Faith must fuel the core of who you are.
The path to freedom begins with asking difficult questions.
Take advantage of every opportunity to educate yourself.
Be your spouse’s protector and advocate.
Radiate humility, vulnerability and love.
Give your finish line the ability to expand.

```html
<!DOCTYPE html>
<html lang="en">
<head>
<meta charset="utf-8">
<title>Life Lessons – Typographic Heart</title>
<link rel="stylesheet" href="https://fonts.googleapis.com/css2?family=Amatic+SC:wght@700&family=Lobster+Two:ital,wght@1,700&family=Montserrat:wght@600;800&family=Oswald:wght@300;500&display=swap">
<style>
  :root {
    --page: #eceeee;
    --board: #16171b;
    --teal: #4db8a6;
    --pink: #ec4c8c;
    --cream: #e4e2c6;
  }
  html, body {
    margin: 0;
    width: 1200px;
    height: 1000px;
    overflow: hidden;
    background: var(--page);
  }
  .poster { display: block; width: 1200px; height: 1000px; }
  .board { fill: var(--board); }
  .frame-outer { fill: none; stroke: var(--cream); stroke-width: 3.5; }
  .frame-inner { fill: none; stroke: var(--pink); stroke-width: 1.5; }
  .teal { fill: var(--teal); }
  .pink { fill: var(--pink); }
  .cream { fill: var(--cream); }
  .bold { font-family: "Montserrat", sans-serif; font-weight: 800; }
  .semi { font-family: "Montserrat", sans-serif; font-weight: 600; }
  .thin { font-family: "Oswald", sans-serif; font-weight: 300; }
  .mid { font-family: "Oswald", sans-serif; font-weight: 500; }
  .hand { font-family: "Amatic SC", sans-serif; font-weight: 700; }
  .script { font-family: "Lobster Two", cursive; font-style: italic; font-weight: 700; }
</style>
</head>
<body>
<svg class="poster" viewBox="0 0 1200 1000" xmlns="http://www.w3.org/2000/svg">
  <rect class="board" x="280" y="63" width="639" height="873"/>
  <path class="frame-outer" d="M341,97 H859 A28,28 0 0 0 887,125 V874 A28,28 0 0 0 859,902 H341 A28,28 0 0 0 313,874 V125 A28,28 0 0 0 341,97 Z"/>
  <path class="frame-inner" d="M352,112 H850 A22,22 0 0 0 872,134 V865 A22,22 0 0 0 850,887 H352 A22,22 0 0 0 330,865 V134 A22,22 0 0 0 352,112 Z"/>

  <!-- small decorations -->
  <rect class="cream" x="505" y="296" width="16" height="14" rx="2" role="img" aria-label="small crown ornament"/>
  <rect class="teal" x="430" y="324" width="28" height="26" rx="8" role="img" aria-label="small bird ornament"/>
  <rect class="pink" x="384" y="379" width="24" height="24" rx="4" role="img" aria-label="snowflake ornament"/>
  <rect class="pink" x="658" y="291" width="60" height="29" rx="14" role="img" aria-label="cloud ornament"/>
  <rect class="teal" x="761" y="326" width="16" height="20" rx="8" role="img" aria-label="flame ornament"/>
  <rect class="cream" x="580" y="340" width="42" height="12" rx="6" role="img" aria-label="flourish ornament"/>
  <polygon class="cream" points="611,383 613,388 618,388 614,391 616,396 611,393 606,396 608,391 604,388 609,388"/>
  <polygon class="cream" points="815,383 817,388 822,388 818,391 820,396 815,393 810,396 812,391 808,388 813,388"/>
  <circle class="pink" cx="511" cy="639" r="6"/>
  <path class="pink" d="M600,696 L593,689 A4,4 0 0 1 600,684 A4,4 0 0 1 607,689 Z"/>
  <rect class="pink" x="616" y="614" width="32" height="31"/>
  <polygon fill="var(--board)" points="632,620 635,627 642,627 636,632 638,639 632,635 626,639 628,632 622,627 629,627"/>

  <!-- left lobe -->
  <text class="script cream" x="532" y="321" font-size="10" text-anchor="middle">Whenever possible</text>
  <text class="script pink" x="463" y="337" font-size="15" textLength="97" lengthAdjust="spacingAndGlyphs"><tspan font-size="10">give </tspan>generously</text>
  <text class="script pink" x="468" y="352" font-size="15" textLength="100" lengthAdjust="spacingAndGlyphs"><tspan font-size="10">and </tspan>anonymously</text>

  <text class="bold teal" x="415" y="381" font-size="30" textLength="183" lengthAdjust="spacingAndGlyphs">MARRIAGE</text>
  <text class="bold teal" x="415" y="395" font-size="12" textLength="183" lengthAdjust="spacingAndGlyphs">IS A UNIFIED FRONT MAKE</text>
  <text class="bold teal" x="415" y="407" font-size="12" textLength="183" lengthAdjust="spacingAndGlyphs">YOUR SPOUSE A PRIORITY</text>

  <text class="semi cream" x="380" y="427" font-size="14" textLength="202" lengthAdjust="spacingAndGlyphs">SELFLESSNESS<tspan font-size="7"> IS A </tspan><tspan class="hand" font-size="21">LIFESTYLE</tspan></text>

  <text class="thin teal" x="374" y="440" font-size="12" textLength="86" lengthAdjust="spacingAndGlyphs">THE PATH TO</text>
  <text class="thin teal" x="368" y="467" font-size="30" textLength="94" lengthAdjust="spacingAndGlyphs">FREEDOM</text>
  <text class="semi teal" x="368" y="481" font-size="13" textLength="94" lengthAdjust="spacingAndGlyphs">BEGINS WITH</text>
  <text class="semi teal" x="368" y="492" font-size="10" textLength="94" lengthAdjust="spacingAndGlyphs">ASKING DIFFICULT</text>
  <text class="semi teal" x="368" y="507" font-size="16" textLength="94" lengthAdjust="spacingAndGlyphs">QUESTIONS</text>
  <text class="semi pink" x="374" y="519" font-size="10" textLength="88" lengthAdjust="spacingAndGlyphs">GIVE YOUR FINISH</text>
  <text class="semi pink" x="378" y="533" font-size="13" textLength="208" lengthAdjust="spacingAndGlyphs">LINE THE ABILITY TO EXPAND</text>

  <text class="semi cream" font-size="12" textLength="46" lengthAdjust="spacingAndGlyphs" transform="translate(479,479) rotate(-90)">DON'T</text>
  <text class="semi cream" x="483" y="440" font-size="9" textLength="102" lengthAdjust="spacingAndGlyphs">LET PEOPLE THAT HURT</text>
  <text class="semi cream" x="483" y="452" font-size="12" textLength="102" lengthAdjust="spacingAndGlyphs">YOU OCCUPY YOUR</text>
  <text class="bold pink" x="484" y="480" font-size="33" textLength="104" lengthAdjust="spacingAndGlyphs">MIND</text>
  <text class="hand cream" x="473" y="499" font-size="21" textLength="109" lengthAdjust="spacingAndGlyphs">WORRYING IS A</text>
  <text class="hand cream" x="473" y="519" font-size="21" textLength="109" lengthAdjust="spacingAndGlyphs">WASTE OF TIME</text>

  <text class="hand teal" x="383" y="554" font-size="18" textLength="202" lengthAdjust="spacingAndGlyphs">FAITH MUST FUEL THE CORE OF WHO</text>
  <text class="semi pink" x="392" y="575" font-size="15" textLength="133" lengthAdjust="spacingAndGlyphs">BE YOUR SPOUSE'S</text>
  <text class="hand cream" x="530" y="575" font-size="21" textLength="52" lengthAdjust="spacingAndGlyphs">YOU ARE</text>
  <text class="semi pink" x="414" y="593" font-size="15" textLength="170" lengthAdjust="spacingAndGlyphs">PROTECTOR &amp; ADVOCATE</text>
  <text class="semi cream" x="443" y="613" font-size="17" textLength="165" lengthAdjust="spacingAndGlyphs">HUMOR DISARMS,</text>
  <text class="semi cream" x="477" y="631" font-size="17" textLength="131" lengthAdjust="spacingAndGlyphs">SOFTENS AND</text>
  <text class="semi cream" x="519" y="647" font-size="17" textLength="89" lengthAdjust="spacingAndGlyphs">ENDEARS</text>

  <text class="semi teal" x="600" y="658" font-size="9" text-anchor="middle" textLength="112" lengthAdjust="spacingAndGlyphs">NEVER APOLOGIZE &amp; GIVE</text>
  <text class="semi teal" x="600" y="670" font-size="9" text-anchor="middle" textLength="94" lengthAdjust="spacingAndGlyphs">EXCUSE IN THE SAME</text>
  <text class="semi teal" x="600" y="682" font-size="9" text-anchor="middle" textLength="50" lengthAdjust="spacingAndGlyphs">SENTENCE</text>

  <!-- central columns -->
  <text class="thin teal" font-size="22" textLength="185" lengthAdjust="spacingAndGlyphs" transform="translate(607,597) rotate(-90)">WORDS<tspan class="bold">MATTER</tspan></text>
  <text class="bold pink" font-size="18" textLength="134" lengthAdjust="spacingAndGlyphs" transform="translate(611,474) rotate(90)">GET OVER IT</text>
  <text class="mid pink" font-size="11" textLength="130" lengthAdjust="spacingAndGlyphs" transform="translate(638,476) rotate(90)">GOOD PEOPLE</text>
  <text class="mid pink" font-size="11" textLength="132" lengthAdjust="spacingAndGlyphs" transform="translate(626,476) rotate(90)">DO BAD THINGS</text>

  <!-- right lobe -->
  <text class="bold cream" x="628" y="340" font-size="15" textLength="124" lengthAdjust="spacingAndGlyphs">NEVER MAKE</text>
  <text class="bold cream" x="628" y="353" font-size="11" textLength="124" lengthAdjust="spacingAndGlyphs">INSINCERE APOLOGIES</text>
  <text class="thin pink" x="616" y="367" font-size="12" textLength="184" lengthAdjust="spacingAndGlyphs">TAKE ADVANTAGE OF EVERY</text>
  <text class="hand pink" x="620" y="402" font-size="42" textLength="188" lengthAdjust="spacingAndGlyphs">OPPORTUNITY</text>
  <text class="thin pink" x="616" y="416" font-size="13" textLength="204" lengthAdjust="spacingAndGlyphs">TO EDUCATE YOURSELF</text>
  <text class="bold teal" x="616" y="430" font-size="12" textLength="212" lengthAdjust="spacingAndGlyphs">FORGIVENESS<tspan class="script" font-size="11"> is not </tspan>OPTIONAL</text>

  <text class="hand cream" x="614" y="455" font-size="25" textLength="119" lengthAdjust="spacingAndGlyphs">TRUTH &amp; GRACE</text>
  <text class="script cream" x="613" y="472" font-size="17" textLength="120" lengthAdjust="spacingAndGlyphs">are inseparable</text>
  <text class="bold pink" x="740" y="448" font-size="15" textLength="95" lengthAdjust="spacingAndGlyphs">CHOOSE YOUR</text>
  <text class="bold pink" x="740" y="473" font-size="25" textLength="96" lengthAdjust="spacingAndGlyphs">DESTINY</text>
  <text class="bold pink" x="740" y="485" font-size="10" textLength="96" lengthAdjust="spacingAndGlyphs">BY CHOOSING YOUR</text>
  <text class="bold pink" x="740" y="510" font-size="23" textLength="93" lengthAdjust="spacingAndGlyphs">FRIENDS</text>

  <text class="semi teal" x="653" y="489" font-size="14" textLength="82" lengthAdjust="spacingAndGlyphs">TAKE EVERY</text>
  <text class="script teal" x="653" y="504" font-size="16" textLength="82" lengthAdjust="spacingAndGlyphs">Opportunity</text>
  <text class="semi teal" x="653" y="519" font-size="14" textLength="82" lengthAdjust="spacingAndGlyphs">TO EXPRESS</text>
  <text class="hand teal" x="653" y="539" font-size="25" textLength="82" lengthAdjust="spacingAndGlyphs">GRATITUDE</text>
  <text class="script cream" x="738" y="525" font-size="14" textLength="98" lengthAdjust="spacingAndGlyphs">Radiate humility,</text>
  <text class="script cream" x="738" y="537" font-size="10" textLength="94" lengthAdjust="spacingAndGlyphs">vulnerability &amp; love</text>

  <text class="hand cream" x="653" y="552" font-size="14" textLength="165" lengthAdjust="spacingAndGlyphs">TRUE BROTHERHOOD IS FORGED OUT OF</text>
  <text class="bold pink" x="653" y="572" font-size="20" textLength="162" lengthAdjust="spacingAndGlyphs">LOYALTY<tspan class="script cream" font-size="18">&amp;</tspan>LOVE</text>
  <text class="semi cream" x="653" y="584" font-size="10" textLength="153" lengthAdjust="spacingAndGlyphs"><tspan class="script">There is no </tspan>EXCUSE<tspan class="script"> for </tspan>DECEIT</text>
  <text class="thin teal" x="653" y="595" font-size="10" textLength="139" lengthAdjust="spacingAndGlyphs">DON'T GIVE UP UNTIL YOU'VE</text>
  <text class="thin teal" x="653" y="609" font-size="16" textLength="119" lengthAdjust="spacingAndGlyphs">GIVEN YOUR ALL</text>
  <text class="hand cream" x="653" y="618" font-size="8" textLength="85" lengthAdjust="spacingAndGlyphs">BLOCK BITTERNESS FROM EVER</text>
  <text class="hand cream" x="653" y="626" font-size="8" textLength="65" lengthAdjust="spacingAndGlyphs">TAKING ROOT IN YOUR</text>
  <text class="hand cream" x="652" y="645" font-size="20" textLength="38" lengthAdjust="spacingAndGlyphs">HEART</text>
</svg>
</body>
</html>
```